The Gemstone Craft Studio Sales Business Card

The goal of this project is to create a interactive & effective business card design for SALES purposes with the intention to get customer on to our website and make a purchase or contact us about a product or service.
Website: WWW.RINGFORGEHUB.COM
GoogleMyBusiness: https://g.page/RingForgeHUB?gm
Facebook & Instagram: @THEGEMSTONECRAFTSTUDIO
Phone # & Text Message & Whatsapp Message: +1(555) 418-0293
Email: HELLO@RINGFORGEHUB.COM
Location: 4872 Brambleton Avenue Suite 512 Maplecrest, VT
(It would be necessary to have the appropriate ticker/icon for each social media platform as well as the location ticker and phone / messaging icons instead of spelling the words out.)
It is important to have the company logo and details but with an emphasis toward website. Feel free to also completely make one design your way and completely custom as you feel best.
The Gemstone Craft Studio is a Provider of Luxury Goods & Services such as: Custom Jewelry Design, Jewelry Repairs & Cleaning, Designer Jewelry, Luxury Gifts, 24 Karat Gold, 22 Karat Gold Jewelry, Diamond Jewelry, Insured Jewelry Appraisals, Loose Gemstones & Diamonds, Supporting Sustainability
Target Market(s)
People looking to invest in precious metals and gemstones as well as people looking to find a gift for a loved one for a special occasion. Customers looking to Custom Design Jewelry.
Contact Information for Business Card
Font styles to use
Other font styles liked:
- w.e you want
Colors
Designer to choose colors to be used in the design.
Requirements
Must have
- Website: WWW.RINGFORGEHUB.COM
- GoogleMyBusiness: https://g.page/RingForgeHUB?gm
- Facebook & Instagram: @THEGEMSTONECRAFTSTUDIO
- Phone # & Text Message & Whatsapp Message: +1(555) 418-0293
- Email: HELLO@RINGFORGEHUB.COM
- Location: 4872 Brambleton Avenue Suite 512 Maplecrest, VT
- (It would be necessary to have the appropriate ticker/icon for each social media platform as well as the location ticker and phone / messaging icons instead of spelling the words out.)
- It is important to have the company logo and details but with an emphasis toward website. Feel free to also completely make one design your way and completely custom as you feel best.
Nice to have
- The Gemstone Craft Studio is a Provider of Luxury Goods & Services such as: Custom Jewelry Design, Jewelry Repairs & Cleaning, Designer Jewelry, Luxury Gifts, 24 Karat Gold, 22 Karat Gold Jewelry, Diamond Jewelry, Insured Jewelry Appraisals, Loose Gemstones & Diamonds, Supporting Sustainability

```html
<!DOCTYPE html>
<html lang="en">
<head>
<meta charset="utf-8">
<title>The Gemstone Craft Studio – Business Card</title>
<link rel="stylesheet" href="https://fonts.googleapis.com/css2?family=Cinzel:wght@400;600;700&family=Fira+Sans:ital,wght@0,300;0,400;1,300&display=swap">
<style>
  :root {
    --bg: #2a2a2a;
    --black: #0c0c0c;
    --white: #ffffff;
    --red: #e3212b;
    --gold: #d8b069;
    --grey: #7d7d7d;
    --light: #e9e9e9;
  }
  * { box-sizing: border-box; margin: 0; padding: 0; }
  html, body { width: 1200px; height: 900px; overflow: hidden; }
  body { background: var(--bg); position: relative; font-family: "Fira Sans", sans-serif; }

  .card { position: absolute; left: 240px; width: 720px; height: 400px; overflow: hidden; }
  .card--back { top: 35px; background: var(--black); }
  .card--front { top: 465px; background: var(--white); }

  /* back side */
  .back__info { position: absolute; left: 0; top: 0; width: 410px; height: 400px; }
  .back__brand { position: absolute; left: 38px; top: 34px; display: flex; align-items: center; gap: 10px;
    font-family: "Cinzel", serif; font-weight: 700; font-size: 17px; color: var(--gold); line-height: 1.15; }
  .brand-square { width: 14px; height: 14px; background: var(--gold); flex: none; }
  .back__url { position: absolute; right: 40px; top: 116px; font-size: 16px; color: var(--white); letter-spacing: .5px; }
  .back__url b { color: var(--red); font-weight: 400; }
  .back__intro { position: absolute; left: 38px; top: 148px; width: 340px; font-family: "Cinzel", serif;
    font-size: 13px; color: var(--gold); line-height: 1.25; }
  .services { position: absolute; left: 38px; top: 194px; list-style: none; }
  .services li { font-size: 15px; font-style: italic; font-weight: 300; color: var(--light); line-height: 20px;
    display: flex; align-items: center; gap: 10px; }
  .services li::before { content: ""; width: 6px; height: 6px; background: var(--gold); flex: none; }
  .back__rule { position: absolute; left: 394px; top: 70px; width: 2px; height: 210px; background: var(--red); }
  .back__map { position: absolute; left: 410px; top: 0; width: 310px; height: 400px;
    background: linear-gradient(160deg, #f6f6f6, #e6e6e6); }

  /* front side */
  .front__band { position: absolute; left: 0; top: 0; width: 720px; height: 120px; background: var(--black); }
  .front__band-block { position: absolute; left: 340px; top: 0; width: 380px; height: 205px; background: var(--black); }
  .front__gold-rule { position: absolute; left: 0; top: 118px; width: 330px; height: 2px; background: var(--gold); }
  .front__red-rule { position: absolute; left: 340px; top: 210px; width: 380px; height: 2px; background: var(--red); }
  .front__title { position: absolute; left: 370px; top: 92px; font-family: "Cinzel", serif; font-weight: 700;
    font-size: 25px; color: var(--red); line-height: 1.05; }
  .front__tagline { position: absolute; left: 370px; top: 160px; font-family: "Cinzel", serif; font-weight: 600;
    font-size: 13px; letter-spacing: 1.5px; color: var(--gold); }

  .front__brand { position: absolute; left: 70px; top: 180px; display: flex; align-items: center; gap: 14px;
    font-family: "Cinzel", serif; font-weight: 700; font-size: 24px; color: var(--gold); line-height: 1.1; }
  .front__brand .brand-square { width: 22px; height: 22px; }
  .social { position: absolute; left: 40px; top: 346px; display: flex; align-items: center; gap: 8px; }
  .social__dot { width: 20px; height: 20px; border-radius: 50%; background: #a9a9a9; }
  .social__handle { margin-left: 4px; font-size: 16px; color: var(--red); font-weight: 400; }

  .person { position: absolute; left: 372px; top: 218px; }
  .person__name { font-family: "Cinzel", serif; font-size: 26px; color: var(--red); line-height: 1; letter-spacing: 1px; }
  .person__role { font-family: "Cinzel", serif; font-size: 13px; color: var(--grey); margin-top: 2px; }
  .contacts { list-style: none; margin-top: 4px; }
  .contacts li { display: flex; align-items: flex-start; gap: 10px; font-size: 15px; font-weight: 300;
    color: var(--grey); line-height: 19px; }
  .contacts svg { width: 15px; height: 15px; margin-top: 2px; flex: none; }
  .contacts .wa { width: 14px; height: 14px; border-radius: 50%; background: var(--red); margin: 2px 1px 0 0; flex: none; }
  .contacts b { color: var(--gold); font-weight: 400; }
</style>
</head>
<body>

<section class="card card--back">
  <div class="back__info">
    <div class="back__brand"><span class="brand-square"></span><span>The Gemstone<br>Craft Studio</span></div>
    <p class="back__url">WWW.<b>RINGFORGEHUB</b>.COM</p>
    <p class="back__intro">The Gemstone Craft Studio is a provider of luxury goods &amp; services such as:</p>
    <ul class="services">
      <li>Custom Jewelry Design</li>
      <li>Jewelry Repairs &amp; Cleaning</li>
      <li>Designer Jewelry, Luxury Gifts</li>
      <li>24 Karat Gold, 22 Karat Gold Jewelry</li>
      <li>Diamond Jewelry, Insured Jewelry Appraisals</li>
      <li>Loose Gemstones &amp; Diamonds</li>
      <li>Supporting Sustainability</li>
    </ul>
  </div>
  <div class="back__rule"></div>
  <div class="back__map" role="img" aria-label="Street map showing the studio location"></div>
</section>

<section class="card card--front">
  <div class="front__band"></div>
  <div class="front__band-block"></div>
  <div class="front__gold-rule"></div>
  <div class="front__red-rule"></div>
  <h1 class="front__title">The Gemstone<br>Craft Studio</h1>
  <p class="front__tagline">REFINED BESPOKE PIECES</p>

  <div class="front__brand"><span class="brand-square"></span><span>The Gemstone<br>Craft Studio</span></div>

  <div class="social">
    <span class="social__dot"></span>
    <span class="social__dot"></span>
    <span class="social__handle">@THEGEMSTONECRAFTSTUDIO</span>
  </div>

  <div class="person">
    <h2 class="person__name">Daniel Whitmore</h2>
    <p class="person__role">Director</p>
    <ul class="contacts">
      <li>
        <svg viewBox="0 0 24 24" fill="none" stroke="#e3212b" stroke-width="2"><path d="M5 3h4l2 5-2.5 1.5a11 11 0 0 0 6 6L16 13l5 2v4a2 2 0 0 1-2 2A17 17 0 0 1 3 5a2 2 0 0 1 2-2z"/></svg>
        +1(555) 418-0293
      </li>
      <li><span class="wa"></span>+1(555) 418-0293</li>
      <li>
        <svg viewBox="0 0 24 24" fill="none" stroke="#e3212b" stroke-width="2"><rect x="2" y="5" width="20" height="14"/><path d="M2 5l10 8 10-8"/></svg>
        HELLO@RINGFORGEHUB.COM
      </li>
      <li>
        <svg viewBox="0 0 24 24" fill="none" stroke="#e3212b" stroke-width="2"><circle cx="12" cy="12" r="10"/><path d="M2 12h20M12 2c3 3 3 17 0 20M12 2c-3 3-3 17 0 20"/></svg>
        <span>WWW.<b>RINGFORGEHUB</b>.COM</span>
      </li>
      <li>
        <svg viewBox="0 0 24 24" fill="none" stroke="#e3212b" stroke-width="2"><path d="M12 22s7-7 7-12a7 7 0 0 0-14 0c0 5 7 12 7 12z"/><circle cx="12" cy="10" r="2.5"/></svg>
        <span>4872 Brambleton Avenue Suite 512<br>Maplecrest, VT</span>
      </li>
    </ul>
  </div>
</section>

</body>
</html>
```